First Aid Training business needs business card design

We would like a double sided business card designed for a first aid training business - Brindlewood First Aid. We provide first aid training and , WHS (work, health and safety) training.

The attached word document contains the key information we would like on each side of the business card.

Final design needs to be delivered in print ready format, along with the original file.

```html
<!DOCTYPE html>
<html lang="en">
<head>
<meta charset="utf-8">
<title>Brindlewood First Aid – Business Card</title>
<link rel="stylesheet" href="https://fonts.googleapis.com/css2?family=Montserrat:wght@500;600&family=Open+Sans:ital,wght@0,400;1,700&display=swap">
<style>
  :root {
    --page: #3a322d;
    --card: #1b1b1c;
    --card-edge: #d41f26;
    --red: #e0262c;
    --white: #f4f4f4;
    --grey-soft: #2a2a2b;
  }
  * { box-sizing: border-box; margin: 0; padding: 0; }
  html, body { width: 1200px; height: 847px; overflow: hidden; background: var(--page); }
  .canvas { position: relative; width: 1200px; height: 847px; }

  .card {
    position: absolute;
    width: 540px; height: 330px;
    background: var(--card);
    border-bottom: 4px solid var(--card-edge);
    overflow: hidden;
    color: var(--white);
    font-family: "Open Sans", sans-serif;
  }
  .card--front { left: 40px; top: 80px; }
  .card--back { left: 620px; top: 437px; }

  .card__ornament {
    position: absolute;
    right: -40px; bottom: -60px;
    width: 320px; height: 320px;
    border-radius: 50%;
    background: radial-gradient(circle at 40% 35%, #2e2e30 0%, #161617 70%);
  }

  .brand {
    font-family: "Montserrat", sans-serif;
    font-weight: 600;
    color: var(--white);
    text-transform: uppercase;
    line-height: 1.05;
  }
  .card--front .brand { position: absolute; left: 34px; top: 30px; font-size: 30px; letter-spacing: 1px; }

  .tagline {
    position: absolute; left: 34px; top: 112px;
    color: var(--red);
    font-style: italic; font-weight: 700;
    font-size: 15px; text-transform: uppercase; line-height: 1.35;
  }
  .benefits {
    position: absolute; left: 34px; top: 162px;
    list-style: none; font-size: 15px; line-height: 1.5;
  }
  .benefits li::before,
  .services .dot {
    content: "";
    display: inline-block;
    width: 8px; height: 8px;
    border: 2px solid var(--red);
    border-radius: 50%;
    margin-right: 8px;
    vertical-align: middle;
  }
  .services {
    position: absolute; left: 34px; top: 262px;
    font-size: 15px;
  }
  .services .dot { margin: 0 10px; }

  .card--back .brand-lockup {
    position: absolute; left: 34px; top: 34px;
    display: flex; align-items: center; gap: 14px;
  }
  .brand-mark {
    width: 44px; height: 44px; border-radius: 50%;
    background: var(--red);
  }
  .card--back .brand { font-size: 24px; letter-spacing: 1px; }

  .person {
    position: absolute; left: 34px; top: 128px;
    color: var(--red);
    font-style: italic; font-weight: 700;
    font-size: 22px; text-transform: uppercase;
  }
  .contacts {
    position: absolute; left: 34px; top: 180px;
    list-style: none; font-size: 16px; line-height: 1.75;
  }
  .contacts li { display: flex; align-items: center; gap: 10px; }
  .contacts svg { width: 14px; height: 14px; fill: var(--red); flex: none; }
</style>
</head>
<body>
<main class="canvas">

  <section class="card card--front" aria-label="Business card front">
    <div class="card__ornament" role="img" aria-label="Large soft dark circle decoration"></div>
    <h1 class="brand">Brindlewood<br>First Aid</h1>
    <p class="tagline">Onsite training<br>We can come to you</p>
    <ul class="benefits">
      <li>Time efficient</li>
      <li>Cost effective</li>
      <li>Minimise downtime for your team</li>
    </ul>
    <p class="services">First Aid Training<span class="dot"></span>WHS Training</p>
  </section>

  <section class="card card--back" aria-label="Business card back">
    <div class="card__ornament" role="img" aria-label="Large soft dark circle decoration"></div>
    <div class="brand-lockup">
      <span class="brand-mark"></span>
      <h2 class="brand">Brindlewood First Aid</h2>
    </div>
    <p class="person">Dana Whitfield</p>
    <ul class="contacts">
      <li>
        <svg viewBox="0 0 24 24" aria-hidden="true"><path d="M6.6 10.8a15 15 0 0 0 6.6 6.6l2.2-2.2a1 1 0 0 1 1-.25 11.4 11.4 0 0 0 3.6.57 1 1 0 0 1 1 1V20a1 1 0 0 1-1 1A17 17 0 0 1 3 4a1 1 0 0 1 1-1h3.5a1 1 0 0 1 1 1c0 1.25.2 2.45.57 3.57a1 1 0 0 1-.25 1z"/></svg>
        0400 555 182
      </li>
      <li>
        <svg viewBox="0 0 24 24" aria-hidden="true"><path d="M2 5h20v14H2z M3 6l9 7 9-7" fill="none" stroke="#e0262c" stroke-width="2"/></svg>
        help@brindlewoodfirstaid.com.au
      </li>
      <li>
        <svg viewBox="0 0 24 24" aria-hidden="true"><circle cx="12" cy="12" r="9" fill="none" stroke="#e0262c" stroke-width="2"/><path d="M3 12h18M12 3c3 3 3 15 0 18M12 3c-3 3-3 15 0 18" fill="none" stroke="#e0262c" stroke-width="1.6"/></svg>
        brindlewoodfirstaid.com.au
      </li>
    </ul>
  </section>

</main>
</body>
</html>
```